Empresa de Asesoramiento en inversiones necesita un nuevo diseño de web

Necesitamos un nuevo diseño de pagina web que nos permita impulsar el posicionamiento de marca en los clientes.
Somos una empresa Española que busca, coordina y gestiona las alternativas de inversión que mejor se ajustan a las necesidades de los Clientes extranjeros, no residentes, para que puedan compra viviendas, locales comerciales o realizar inversiones en sociedades y startup en España.
En la actualidad tenemos esta web que puede servir de referencia; www.brixolacapital,com
El diseño final debe comunicar seguridad y responsabilidad en los procesos de inversión.
Necesitamos que la Pagina web sea bilingüe ( Español-Ingles)

```html
<!DOCTYPE html>
<html lang="en">
<head>
<meta charset="utf-8">
<title>BrixolaCapital – Investment In Spain</title>
<link href="https://fonts.googleapis.com/css2?family=Lato:wght@400;700;900&display=swap" rel="stylesheet">
<style>
:root{
  --blue:#2b3a80;
  --dark:#2a2a2e;
  --footer:#2c2c31;
  --text:#4a4a4a;
  --ink:#111;
  --white:#fff;
  --dot:#dadada;
}
*{box-sizing:border-box;margin:0;padding:0}
html,body{width:1200px;height:3437px;overflow:hidden;background:var(--white);font-family:'Lato',sans-serif;color:var(--ink)}
.page{position:relative;width:1200px;height:3437px;overflow:hidden}
.abs{position:absolute}
.photo{position:absolute}
.dots{position:absolute;background:#f1f1f3}
/* header */
.logo{left:143px;top:22px;font-size:38px;font-weight:900;letter-spacing:-.3px;color:var(--ink)}
.head-mail{left:672px;top:6px;display:flex;align-items:center;gap:8px;font-size:17px;font-weight:700;color:var(--ink)}
.mail-ico{width:40px;height:40px}
.lang{left:1012px;top:14px;font-size:13px;font-weight:700;color:var(--blue)}
.nav{top:61px;display:flex;font-size:12.5px;letter-spacing:.2px}
.nav a{color:var(--ink);text-decoration:none;position:absolute;white-space:nowrap}
.nav a.active::after{content:"";position:absolute;left:0;right:0;bottom:-10px;height:3px;background:var(--blue)}
/* hero */
.hero-panel{left:710px;top:91px;width:490px;height:427px;background:var(--blue)}
.hero-title{left:763px;top:190px;color:var(--white);font-size:56px;font-weight:900;line-height:59px}
.btn{position:absolute;display:flex;align-items:center;justify-content:center;font-size:15px;font-weight:900;text-decoration:none;border:2px solid}
.btn-light{color:var(--white);border-color:var(--white)}
.btn-dark{color:var(--blue);border-color:var(--blue);background:var(--white)}
.slider-dots{left:1134px;top:444px;width:12px}
.slider-dots span{display:block;width:6px;height:6px;border-radius:50%;background:var(--white);margin:0 auto 7px}
.slider-dots span.on{width:12px;height:12px;background:none;border:2px solid var(--white)}
.frame{left:144px;top:467px;width:911px;height:400px;background:var(--white)}
/* sections */
.rule{position:absolute;width:4px;background:var(--blue)}
.h2{position:absolute;font-size:56px;font-weight:900;line-height:1}
.copy{position:absolute;font-size:15px;line-height:27px;color:var(--text)}
.phil-panel{left:561px;top:1304px;width:639px;height:414px;background:var(--blue)}
.obj-panel{left:0;top:1889px;width:641px;height:413px;background:var(--dark)}
.ticks{left:144px;top:2030px;width:440px;list-style:none;color:var(--white);font-size:15px;line-height:27px}
.ticks li{position:relative;padding-left:31px;text-align:justify}
.ticks svg{position:absolute;left:0;top:7px;width:16px;height:13px}
/* blog */
.tab{position:absolute;height:42px;border:2px solid var(--blue);display:flex;align-items:center;justify-content:center;font-size:15.5px;color:var(--ink);background:var(--white)}
.tab.on{background:var(--blue);color:var(--white);font-weight:900;font-size:18px}
.card-title{position:absolute;font-size:16.5px;font-weight:700;color:var(--ink)}
.card-meta{position:absolute;width:262px;font-size:13.5px;line-height:22.5px;color:var(--text);text-align:justify}
.read{position:absolute;font-size:19px;font-weight:900;color:var(--blue)}
.feature{left:455px;top:2916px;width:290px;height:105px;background:var(--blue);color:var(--white);text-align:center}
.feature b{display:block;margin-top:20px;font-size:17px;font-weight:700}
.feature small{display:block;margin-top:8px;font-size:11.5px}
/* footer */
.footer{left:0;top:3211px;width:1200px;height:226px;background:var(--footer)}
.foot-nav a{position:absolute;top:3256px;color:var(--white);font-size:14px;text-decoration:none;white-space:nowrap}
.foot-line{left:0;top:3315px;width:1200px;height:1px;background:#45454b}
.social{position:absolute;top:3350px;width:50px;height:50px;border-radius:50%;background:var(--white)}
.legal{right:145px;top:3366px;font-size:14px;color:var(--white)}
</style>
</head>
<body>
<div class="page">

  <!-- Header -->
  <div class="abs logo">BrixolaCapital</div>
  <div class="abs head-mail">
    <svg class="mail-ico" viewBox="0 0 40 40"><circle cx="20" cy="20" r="18" fill="none" stroke="#2b3a80" stroke-width="2"/><rect x="10" y="13" width="20" height="14" fill="none" stroke="#2b3a80" stroke-width="2"/><path d="M10 13l10 8 10-8M10 27l7-6M30 27l-7-6" fill="none" stroke="#2b3a80" stroke-width="1.6"/></svg>
    inquiries@brixolacapital.com
  </div>
  <div class="abs lang">EN ▾</div>
  <nav class="abs nav">
    <a class="active" style="left:526px">HOME</a>
    <a style="left:592px">HOW WE WORK</a>
    <a style="left:718px">SUCCESSFUL INVESTMENTS</a>
    <a style="left:913px">CONTACT</a>
    <a style="left:1000px">PRESENT</a>
  </nav>

  <!-- Hero -->
  <div class="photo" role="img" aria-label="Photo of a historic stone gate monument in Madrid under a blue sky" style="left:0;top:91px;width:693px;height:427px;background:linear-gradient(180deg,#4f7fc9 0%,#8aa4c8 35%,#8c8880 60%,#5b6a4a 90%,#b03a4a 100%)"></div>
  <div class="abs hero-panel"></div>
  <h1 class="abs hero-title">Investment<br>In Spain</h1>
  <a class="btn btn-light" style="left:765px;top:354px;width:151px;height:52px">GET IN TOUCH</a>
  <div class="abs slider-dots"><span class="on"></span><span></span><span></span></div>
  <div class="abs frame"></div>
  <div class="photo" role="img" aria-label="Photo of advisors reviewing a budget chart on a laptop at a meeting table" style="left:159px;top:481px;width:882px;height:380px;background:linear-gradient(110deg,#3a3f4e 0%,#8b8a86 35%,#d7d3cc 55%,#9aa2ad 80%,#5d6676 100%)"></div>
  <div class="dots" role="img" aria-label="Decorative dot grid" style="left:87px;top:541px;width:48px;height:196px"></div>

  <!-- About -->
  <div class="rule" style="left:220px;top:848px;height:313px"></div>
  <div class="dots" role="img" aria-label="Decorative dot grid" style="left:549px;top:882px;width:196px;height:52px"></div>
  <h2 class="h2" style="left:282px;top:930px">About</h2>
  <p class="copy" style="left:282px;top:1000px;width:740px">We are a great team of professionals and associated companies, in Spain and Latin America, with the mission of supporting you in your " Investment in Spain" project. We coordinate, supervise and manage the entire investment process so that non-resident foreigners can buy homes , commercial premises or make investments in companies and startups in Spain.</p>

  <!-- Philosophy -->
  <div class="dots" role="img" aria-label="Decorative dot grid" style="left:1004px;top:1180px;width:196px;height:114px"></div>
  <div class="abs phil-panel"></div>
  <div class="photo" role="img" aria-label="Photo of hands working at a laptop with stock charts and printed reports" style="left:144px;top:1225px;width:462px;height:440px;background:linear-gradient(135deg,#e6e6e4 0%,#9a9ea6 40%,#4a5064 70%,#c9ccd3 100%)"></div>
  <div class="dots" role="img" aria-label="Decorative dot grid" style="left:47px;top:1552px;width:196px;height:200px"></div>
  <h2 class="h2" style="left:670px;top:1370px;color:var(--white)">Our Philosophy</h2>
  <p class="copy" style="left:672px;top:1444px;width:347px;color:var(--white);text-align:justify">Help you to invest in Spain in a safe and profitable way, complying with all the investment processes in Spain and accessing the residence visa for investment.</p>
  <a class="btn btn-light" style="left:670px;top:1594px;width:135px;height:52px">READ MORE</a>

  <!-- Objectives -->
  <div class="abs obj-panel"></div>
  <div class="photo" role="img" aria-label="Photo of an investor using a tablet and laptop with rising financial chart overlay" style="left:593px;top:1786px;width:462px;height:438px;background:linear-gradient(150deg,#2e3540 0%,#6b5f50 45%,#a58b66 70%,#3b4250 100%)"></div>
  <div class="dots" role="img" aria-label="Decorative dot grid" style="left:914px;top:2105px;width:196px;height:200px"></div>
  <h2 class="h2" style="left:144px;top:1958px;color:var(--white)">Our Objectives</h2>
  <ul class="abs ticks">
    <li><svg viewBox="0 0 16 13"><path d="M1 7l5 4 9-10" fill="none" stroke="#fff" stroke-width="2.6"/></svg>Find you the best and most profitable investment opportunities in Spain.</li>
    <li><svg viewBox="0 0 16 13"><path d="M1 7l5 4 9-10" fill="none" stroke="#fff" stroke-width="2.6"/></svg>Support you throughout the process with transparency, honesty and always seeking your highest profitability.</li>
  </ul>
  <a class="btn btn-light" style="left:144px;top:2179px;width:135px;height:52px">READ MORE</a>

  <!-- Blog -->
  <div class="rule" style="left:144px;top:2302px;height:315px"></div>
  <h2 class="h2" style="left:207px;top:2375px">My Blog</h2>
  <div class="tab on" style="left:147px;top:2479px;width:123px">All Posts</div>
  <div class="tab" style="left:276px;top:2479px;width:162px">Mortgage credits</div>
  <div class="tab" style="left:444px;top:2479px;width:220px">Real Estate Market Studies</div>
  <div class="tab" style="left:668px;top:2479px;width:219px">Investments in Companies</div>
  <div class="tab" style="left:892px;top:2479px;width:162px">Investment News</div>
  <div class="tab" style="left:157px;top:2531px;width:219px">Non-resident loans</div>
  <div class="tab" style="left:382px;top:2531px;width:217px">Residence visa Spain</div>

  <div class="photo" role="img" aria-label="Photo of a woman working on a laptop in a cafe" style="left:146px;top:2642px;width:290px;height:200px;background:linear-gradient(120deg,#c8a273 0%,#8a5a36 45%,#b8462f 70%,#6c5a4a 100%)"></div>
  <div class="card-title" style="left:150px;top:2862px">Individuals access FACTORING</div>
  <p class="card-meta" style="left:152px;top:2899px">October 29, 2020 | Mortgage loans, Real Estate Market Studies, Investments in Companies, INVESTMENT NEWS, Non-resident loans, Residence visa Spain</p>
  <div class="read" style="left:151px;top:3004px">READ MORE</div>

  <div class="photo" role="img" aria-label="Abstract image of a glowing particle helix on a black background" style="left:455px;top:2642px;width:290px;height:274px;background:radial-gradient(ellipse at 60% 40%,#3f6a80 0%,#112029 40%,#000 75%)"></div>
  <div class="abs feature"><b>VERANO FINANCE expands Capital</b><small>October 29, 2020 | INVESTMENT NEWS</small></div>

  <div class="photo" role="img" aria-label="Photo of two hands sheltering a small wooden house figure" style="left:765px;top:2642px;width:290px;height:200px;background:linear-gradient(135deg,#3a2a22 0%,#6e5040 45%,#c7a58a 60%,#3e2e26 100%)"></div>
  <div class="card-title" style="left:769px;top:2862px">Benefits of residence visa for investment</div>
  <p class="card-meta" style="left:771px;top:2899px">In Spain , the residence visa for invest-ment covers the buyer, his/her spouse and children under 18 years of age.This visa allows the investor and his family</p>
  <div class="read" style="left:770px;top:3004px">READ MORE</div>

  <a class="btn btn-dark" style="left:503px;top:3082px;width:194px;height:52px">LOAD MORE NEWS</a>
  <div class="dots" role="img" aria-label="Decorative dot grid" style="left:1004px;top:3109px;width:196px;height:96px"></div>

  <!-- Footer -->
  <footer class="abs footer"></footer>
  <div class="foot-nav">
    <a style="left:144px">HOME</a>
    <a style="left:214px">HOW WE WORK</a>
    <a style="left:347px">SUCCESSFUL INVESTMENTS</a>
    <a style="left:555px">CONTACT</a>
    <a style="left:647px">PRESENT</a>
  </div>
  <div class="abs head-mail" style="left:736px;top:3243px;color:var(--white)">
    <svg class="mail-ico" viewBox="0 0 40 40"><circle cx="20" cy="20" r="18" fill="none" stroke="#fff" stroke-width="2"/><rect x="10" y="13" width="20" height="14" fill="none" stroke="#fff" stroke-width="2"/><path d="M10 13l10 8 10-8M10 27l7-6M30 27l-7-6" fill="none" stroke="#fff" stroke-width="1.6"/></svg>
    inquiries@brixolacapital.com
  </div>
  <div class="abs foot-line"></div>
  <div class="social" style="left:146px"></div>
  <div class="social" style="left:218px"></div>
  <div class="social" style="left:291px"></div>
  <div class="abs legal">Copyright © 2022 Brixolacapital - All Rights Reserved &nbsp;| &nbsp;Privacy &nbsp;| &nbsp;Terms of Use</div>

</div>
</body>
</html>
```